Updated web design for software design firm supporting entrepreneurs

Looking for a more modern looking, mobile friendly website design for our company, Brainwave2Binaries. B2B is a software development firm who supports people who have ideas for software and want to make them a reality. It also provides some maintenance work on existing websites as well as mobile apps. Please see our current website, www.brainwave2binaries-example.com, for more information on our business.

Old logo files included for reference. However, we are hoping to incorporate a new logo.

Like a blue'ish theme, but open to ideas.

Industry/Entity Type

Software

Logo Text

B2B and/or Brainwave2Binaries

Number of Pages Required

2 page

Font styles to use
Serif
Sans Serif

Colors
33a6d7
0255a3

Requirements
Must have
• Looking for 2 pages designed: 1 landing page and 1 type of secondary content page
• Please prepare menu for about 7 pages
Nice to have
• This will be implemented as a WordPress theme.
• Could include post-it note, white board, napkins, etc.

```html
<!DOCTYPE html>
<html lang="en">
<head>
<meta charset="utf-8">
<title>Brainwave2Binaries</title>
<link href="https://fonts.googleapis.com/css2?family=Lato:wght@300;400;700&family=Ubuntu:wght@400;500&display=swap" rel="stylesheet">
<style>
:root{
  --blue:#0255a3;
  --sky:#33a6d7;
  --ink:#333;
  --muted:#777;
  --grey:#f0f0f0;
  --dark:#141414;
  --footer:#262626;
  --teal:#5aa3a8;
  --band:rgba(20,90,170,.82);
}
*{margin:0;padding:0;box-sizing:border-box}
html,body{width:1200px;height:2643px;overflow:hidden}
body{font-family:'Lato',sans-serif;color:var(--ink);background:#fff;position:relative}
.section{position:absolute;left:0;width:1200px}
.section-title{font-weight:400;color:var(--sky);font-size:21px;text-align:center}
.section-title::after{content:"";display:block;width:34px;height:2px;background:var(--sky);margin:10px auto 0}

/* header */
.site-header{top:0;height:88px;background:#fff}
.brand{position:absolute;left:206px;top:24px;display:flex;align-items:center;gap:10px;font-weight:700;font-size:30px;color:var(--blue)}
.brand-dot{width:16px;height:16px;border-radius:50%;background:var(--sky)}
.top-phones{position:absolute;left:763px;top:22px;display:flex;gap:16px;font-size:13px;color:var(--sky)}
.top-phones span{display:flex;align-items:center;gap:6px}
.main-nav{position:absolute;left:455px;top:53px;display:flex;gap:20px;font-size:10.5px;font-weight:700;letter-spacing:.5px}
.main-nav a{color:#333;text-decoration:none}
.main-nav a.active{color:var(--sky)}

/* hero */
.hero{top:88px;height:338px;background:linear-gradient(100deg,#0d1620 0%,#1e2a38 35%,#3a3a3c 65%,#161616 100%)}
.hero h1{position:absolute;top:105px;width:100%;text-align:center;color:#fff;font-weight:400;font-size:30px}
.hero h2{position:absolute;top:146px;width:100%;text-align:center;color:var(--sky);font-weight:400;font-size:23px;letter-spacing:.5px}
.hero-actions{position:absolute;top:200px;width:100%;display:flex;justify-content:center;gap:14px}
.btn{display:inline-block;font-size:10px;font-weight:700;letter-spacing:1px;color:#fff;padding:8px 14px;text-transform:uppercase}
.btn-sky{background:var(--sky)}
.btn-blue{background:var(--blue)}
.hero-arrow{position:absolute;top:148px}

/* who we are */
.who{top:426px;height:349px}
.who h3{position:absolute;left:255px;top:44px;color:var(--sky);font-weight:400;font-size:19px}
.who h3::after{content:"";display:block;width:30px;height:2px;background:var(--sky);margin-top:10px}
.who-text{position:absolute;left:255px;top:100px;width:350px;font-size:12.5px;line-height:1.6;color:#555}
.who-text p{margin-bottom:12px}
.who .btn{position:absolute;left:255px;top:260px;padding:7px 18px;display:flex;gap:8px;align-items:center}
.who-photo{position:absolute;left:655px;top:50px;width:291px;height:257px;background:linear-gradient(135deg,#dfe6ee,#8fa3b8 60%,#2e3a4a)}

/* how it works */
.how{top:775px;height:323px;background:var(--grey)}
.how .section-title{position:absolute;top:40px;width:100%}
.how-lead{position:absolute;top:86px;width:100%;text-align:center;font-size:12px;color:#999}
.step{position:absolute;top:136px;width:260px;text-align:center}
.step-icon{width:63px;height:63px;border-radius:50%;background:var(--sky);margin:0 auto;display:flex;align-items:center;justify-content:center}
.step h4{font-weight:400;font-size:16px;margin:10px 0 6px}
.step p{font-size:10.5px;line-height:1.5;color:#666}

/* portfolio */
.portfolio{top:1098px;height:609px}
.portfolio .section-title{position:absolute;top:38px;width:100%}
.tiles{position:absolute;top:102px;left:0;display:grid;grid-template-columns:repeat(4,300px);grid-template-rows:254px 253px}
.tile{position:relative;overflow:hidden}
.tile-label{position:absolute;left:0;bottom:0;width:100%;height:54px;background:var(--band);color:#fff;font-family:'Ubuntu',sans-serif;font-size:21px;display:flex;align-items:center;justify-content:center}
.tile-overlay{position:absolute;inset:0;background:rgba(40,100,190,.55);color:#fff;text-align:center;padding-top:60px}
.tile-overlay h5{font-family:'Ubuntu',sans-serif;font-weight:400;font-size:20px}
.tile-overlay p{font-size:10.5px;line-height:1.45;width:200px;margin:10px auto 16px}
.btn-white{background:#fff;color:var(--blue);padding:7px 16px}
.tile-promo{background:var(--blue);color:#fff;text-align:center;padding-top:66px}
.tile-promo .name{font-size:16px;letter-spacing:.5px}
.tile-promo .tag{font-size:16px;line-height:1.55;margin-top:4px}
.tile-promo .btn-white{margin-top:16px;font-size:9px}

/* testimonial */
.testimonial{top:1707px;height:273px}
.testimonial .section-title{position:absolute;top:40px;width:100%}
.quote{position:absolute;top:115px;left:210px;width:780px;text-align:center;font-size:11.5px;line-height:1.6;color:#666}
.quote-icon{position:absolute;top:175px;left:582px}
.quote-name{position:absolute;top:216px;width:100%;text-align:center;font-size:12px;color:#444}
.t-arrow{position:absolute;top:120px}

/* contact strip */
.contact-strip{top:1980px;height:208px;background:var(--grey)}
.contact-col{position:absolute;top:42px;width:260px;text-align:center;font-size:11px;color:#555;line-height:1.5}
.contact-col .big{font-size:17px;color:#222}
.contact-col .label{font-size:11.5px;color:#222}
.contact-col a{color:var(--blue)}
.divider{position:absolute;top:32px;height:120px;border-left:1px dotted #999}

/* form and map */
.touch{top:2188px;height:384px;width:600px;background:var(--dark)}
.touch h4{position:absolute;left:206px;top:52px;color:#fff;font-size:13px;font-weight:700}
.field{position:absolute;border-bottom:1px solid #555;color:#888;font-size:10.5px;padding-bottom:10px}
.send{position:absolute;left:208px;top:312px;width:85px;height:28px;background:var(--teal);color:#fff;font-size:11px;display:flex;align-items:center;justify-content:center;gap:6px}
.map{top:2188px;left:600px;width:600px;height:384px;background:linear-gradient(160deg,#f2f2f2,#e2e2e2 50%,#eeeeee)}
.map-pin{position:absolute;left:281px;top:156px}

/* footer */
.site-footer{top:2572px;height:71px;background:var(--footer)}
.copyright{position:absolute;left:208px;top:30px;color:#bbb;font-size:10.5px}
.social{position:absolute;left:768px;top:24px;display:flex;gap:5px}
.social span{width:20px;height:20px;border-radius:50%;background:#888}
.to-top{position:absolute;left:1032px;top:14px}
</style>
</head>
<body>

<header class="section site-header">
  <div class="brand"><span class="brand-dot"></span>B2B</div>
  <div class="top-phones">
    <span><svg width="14" height="14" viewBox="0 0 14 14"><circle cx="7" cy="7" r="6.3" fill="none" stroke="#33a6d7"/><path d="M4.5 4c.6 2.6 2.4 4.5 5 5.2l.6-1.2-1.3-.7-.6.6c-1-.5-1.8-1.3-2.3-2.3l.6-.6-.7-1.3z" fill="#33a6d7"/></svg>(555) 013-4827</span>
    <span><svg width="14" height="14" viewBox="0 0 14 14"><circle cx="7" cy="7" r="6.3" fill="none" stroke="#33a6d7"/><circle cx="7" cy="7" r="2.5" fill="#33a6d7"/></svg>(555) 013-4827</span>
  </div>
  <nav class="main-nav">
    <a class="active" href="#">HOME</a><a href="#">WHO WE ARE</a><a href="#">HOW IT WORKS</a><a href="#">WHO NEEDS US</a><a href="#">ODD JOBS</a><a href="#">PORTFOLIO</a><a href="#">CONTACT US</a>
  </nav>
</header>

<section class="section hero" role="img" aria-label="Photo of code on a monitor beside a coffee mug on a desk">
  <svg class="hero-arrow" style="left:122px" width="30" height="56" viewBox="0 0 30 56"><path d="M26 2L4 28l22 26" fill="none" stroke="#fff" stroke-width="2"/></svg>
  <svg class="hero-arrow" style="left:1050px" width="30" height="56" viewBox="0 0 30 56"><path d="M4 2l22 26L4 54" fill="none" stroke="#fff" stroke-width="2"/></svg>
  <h1>How do I get a Piece of Working Software?</h1>
  <h2>First, come up with your Idea</h2>
  <div class="hero-actions"><span class="btn btn-sky">Learn More</span><span class="btn btn-blue">Consult Now</span></div>
</section>

<section class="section who">
  <h3>Who We Are</h3>
  <div class="who-text">
    <p>Brainwave2Binaries can help anyone turn their software idea into reality. We understand that you don't have to be a big company to have big ideas, but turning those ideas into functional software can be time consuming, expensive and seem out of reach.</p>
    <p>As a small business ourselves, we understand the need to be flexible, efficient and cost-conscious.</p>
  </div>
  <span class="btn btn-blue"><svg width="11" height="11" viewBox="0 0 11 11"><circle cx="5.5" cy="5.5" r="5" fill="#fff"/></svg>Contact Us</span>
  <div class="who-photo" role="img" aria-label="Photo of business people reviewing charts on a tablet"></div>
</section>

<section class="section how">
  <h3 class="section-title">How it Works</h3>
  <p class="how-lead">How do I get a piece of working software? First, come up with your idea.</p>
  <div class="step" style="left:191px">
    <div class="step-icon"><svg width="30" height="30" viewBox="0 0 30 30" fill="none" stroke="#fff" stroke-width="2"><path d="M15 5a7 7 0 0 0-4 12.7V21h8v-3.3A7 7 0 0 0 15 5z"/><path d="M12 24h6"/></svg></div>
    <h4>Idea</h4>
    <p>Brainwave2Binaries can help anyone turn their<br>software idea into reality. We understand<br>that you don't have.</p>
  </div>
  <div class="step" style="left:480px">
    <div class="step-icon"><svg width="32" height="32" viewBox="0 0 32 32" fill="none" stroke="#fff" stroke-width="2"><circle cx="20" cy="8" r="3.5"/><circle cx="8" cy="24" r="3.5"/><circle cx="24" cy="24" r="3.5"/><path d="M18 11l-8 10M11.5 24h9"/></svg></div>
    <h4>Plan</h4>
    <p>During the consultation and the communications<br>that follow, a plan of action will be<br>developed.</p>
  </div>
  <div class="step" style="left:747px">
    <div class="step-icon"><svg width="32" height="32" viewBox="0 0 32 32" fill="none" stroke="#fff" stroke-width="2"><rect x="5" y="7" width="22" height="15"/><path d="M12 27h8M16 22v5"/><circle cx="16" cy="14.5" r="3"/></svg></div>
    <h4>Develop</h4>
    <p>Brainwave2Binaries will then produce a develop-<br>ment plan which will include both time<br>and cost.</p>
  </div>
</section>

<section class="section portfolio">
  <h3 class="section-title">Portfolio</h3>
  <div class="tiles">
    <div class="tile" style="background:#1b7f92" role="img" aria-label="Illustration of a presenter with a megaphone beside video thumbnails"><div class="tile-label">Video Projects</div></div>
    <div class="tile" style="background:#3a6fb8" role="img" aria-label="Illustration of a social network of people and icons">
      <div class="tile-overlay"><h5>Social Networking</h5><p>We have built a variety of social networking applications that were inspired by well known social media platforms....</p><span class="btn btn-white">Read More</span></div>
    </div>
    <div class="tile" style="background:#5ec3b0" role="img" aria-label="Illustration of a hand holding a smartphone with app icons"><div class="tile-label">Mobile Apps</div></div>
    <div class="tile" style="background:#dcd8cc" role="img" aria-label="Street map with a location marker"><div class="tile-label">Mapping Software</div></div>
    <div class="tile" style="background:#5aa8b6" role="img" aria-label="Illustration of a hand holding a stopwatch with publishing charts"><div class="tile-label">Online Publishing</div></div>
    <div class="tile" style="background:#6a1420" role="img" aria-label="Illustration of a figure surrounded by app icons"><div class="tile-label">API Integration</div></div>
    <div class="tile" style="background:#5cc0e6" role="img" aria-label="Illustration of hands exchanging a card and a shopping bag"><div class="tile-label">E-commerce</div></div>
    <div class="tile tile-promo">
      <div class="name">BRAINWAVE2BINARIES, LLC</div>
      <div class="tag">turning your software<br>vision into reality</div>
      <span class="btn btn-white">Contact Us</span>
    </div>
  </div>
</section>

<section class="section testimonial">
  <h3 class="section-title">Testimonial</h3>
  <svg class="t-arrow" style="left:138px" width="20" height="40" viewBox="0 0 20 40"><path d="M18 2L3 20l15 18" fill="none" stroke="#999" stroke-width="1.5"/></svg>
  <svg class="t-arrow" style="left:1040px" width="20" height="40" viewBox="0 0 20 40"><path d="M2 2l15 18L2 38" fill="none" stroke="#0255a3" stroke-width="1.5"/></svg>
  <p class="quote">"Many desktop publishing packages and web page editors now use Lorem Ipsum as their default model text, and a search for 'lorem ipsum' will uncover many web sites still in their infancy. Various versions have evolved over the years, sometimes by accident, sometimes on purpose (injected humour and the like)."</p>
  <svg class="quote-icon" width="36" height="36" viewBox="0 0 36 36"><circle cx="18" cy="18" r="16" fill="none" stroke="#33a6d7" stroke-width="2"/><path d="M10 12h16v9H16l-4 4v-4h-2z" fill="#33a6d7"/></svg>
  <p class="quote-name">Dana Whitfield</p>
</section>

<section class="section contact-strip">
  <div class="contact-col" style="left:217px">
    <svg width="40" height="40" viewBox="0 0 40 40"><path d="M11 6c2 10 9 20 22 24l3-5-6-4-3 3c-5-2-9-6-11-11l3-3-4-6z" fill="none" stroke="#555" stroke-width="1.5"/></svg>
    <div class="big">Call: (555) 013-4827</div>
    <div>Skype: (555) 013-4827</div>
  </div>
  <div class="divider" style="left:477px"></div>
  <div class="contact-col" style="left:481px">
    <svg width="40" height="40" viewBox="0 0 40 40"><path d="M20 37S8 22 8 15a12 12 0 0 1 24 0c0 7-12 22-12 22z" fill="none" stroke="#555" stroke-width="1.5"/><circle cx="20" cy="15" r="4" fill="none" stroke="#555" stroke-width="1.5"/></svg>
    <div class="label">BRAINWAVE2BINARIES, LLC</div>
    <div>4120 NE. Maple Row</div>
    <div>Harbor Glen, IN 46000</div>
  </div>
  <div class="divider" style="left:747px"></div>
  <div class="contact-col" style="left:777px">
    <svg width="44" height="40" viewBox="0 0 44 40"><rect x="3" y="8" width="38" height="26" fill="none" stroke="#555" stroke-width="1.5"/><path d="M3 8l19 15L41 8" fill="none" stroke="#555" stroke-width="1.5"/></svg>
    <div class="label">E-mail Us</div>
    <div><a>questions@brainwave2binaries-example.com</a></div>
  </div>
</section>

<section class="section touch">
  <h4>Keep in touch with us</h4>
  <div class="field" style="left:208px;top:100px;width:314px">Name</div>
  <div class="field" style="left:208px;top:150px;width:180px">Email</div>
  <div class="field" style="left:409px;top:150px;width:113px">Phone</div>
  <div class="field" style="left:208px;top:200px;width:314px;height:75px">Message</div>
  <div class="send"><svg width="11" height="11" viewBox="0 0 11 11"><path d="M1 5l9-4-3 9-2-3z" fill="#fff"/></svg>Send</div>
</section>

<section class="section map" role="img" aria-label="Grey area map with a location marker">
  <svg class="map-pin" width="30" height="40" viewBox="0 0 30 40"><path d="M15 39S3 23 3 14a12 12 0 0 1 24 0c0 9-12 25-12 25z" fill="#0255a3"/><circle cx="15" cy="14" r="4" fill="#fff"/></svg>
</section>

<footer class="section site-footer">
  <div class="copyright">© 2016 BRAINWAVE2BINARIES, LLC.</div>
  <div class="social"><span></span><span></span><span></span><span></span><span></span><span></span></div>
  <svg class="to-top" width="34" height="38" viewBox="0 0 34 38"><path d="M3 2h28M17 36V9M8 18l9-9 9 9" fill="none" stroke="#33a6d7" stroke-width="2"/></svg>
</footer>

</body>
</html>
```